Bluestone Advisory & Mgmt - Professional Business Cards

Hi!

I am a Real Estate Developer and Construction Consultant.

I have a lot of inspiration from previous designs and would be open to using the attached Designs as a starting point. I would like to see these styles incorporated into your designs.

I really need professional business card to go with it that includes my important info.

Look forward to seeing your designs!.

Target Market(s)

My Target market are building owners, lawyers, consultants.

Industry/Entity Type

Real Estate Development

Contact Information for Business Card

My Name: Dorian Pelkey
My Title: Principle
Company Name: Bluestone Advisory & Mgmt, LLC
Address: 348 West 71st Street, 9th FL New York, NY 10010
Mobile: 917.806.3971
Website: bam-hvx.example

Font styles to use
Serif
Sans Serif

Colors

Designer to choose colors to be used in the design.

Requirements
Must have
• Must incorporate the logo attached or have new that looks similar.
• Must use professional font that will be seen and judged by wealthy land owners and developers.
• Must incorporate some of the color green.
Should not have
• Photo's or pictures of people or buildings of any kind.

```html
<!DOCTYPE html>
<html lang="en">
<head>
<meta charset="utf-8">
<title>Bluestone Advisory &amp; Mgmt - Business Cards</title>
<link href="https://fonts.googleapis.com/css2?family=Poppins:wght@300;400;600&family=Arimo:wght@400&display=swap" rel="stylesheet">
<style>
  :root {
    --backdrop: #d4d4d4;
    --card-white: #ffffff;
    --brand-green: #3db36f;
    --deep-green: #2a9a59;
    --warm-grey: #8c8383;
    --ink: #2b2b2b;
  }
  * { box-sizing: border-box; margin: 0; padding: 0; }
  html, body { width: 1200px; height: 800px; overflow: hidden; }
  body {
    background: var(--backdrop);
    display: flex;
    align-items: center;
    justify-content: center;
    gap: 40px;
  }
  .card {
    width: 560px;
    height: 320px;
    border-radius: 22px;
    position: relative;
    box-shadow: 0 6px 18px rgba(0,0,0,0.18);
  }
  .card-front { background: var(--card-white); }
  .card-back {
    background: var(--brand-green);
    display: flex;
    align-items: center;
    justify-content: center;
  }
  .wordmark {
    font-family: "Poppins", sans-serif;
    font-weight: 300;
    line-height: 1.05;
    display: flex;
    align-items: center;
    gap: 12px;
  }
  .wordmark-dot {
    width: 18px; height: 18px; border-radius: 50%;
    background: currentColor;
    flex: none;
  }
  .card-front .wordmark {
    position: absolute;
    top: 38px;
    right: 40px;
    color: var(--brand-green);
    font-size: 26px;
  }
  .card-back .wordmark {
    color: var(--deep-green);
    font-size: 34px;
  }
  .contact {
    position: absolute;
    left: 40px;
    bottom: 36px;
    font-family: "Arimo", sans-serif;
    color: var(--ink);
  }
  .contact-name {
    font-family: "Poppins", sans-serif;
    font-weight: 600;
    font-size: 22px;
    color: var(--brand-green);
    line-height: 1.1;
  }
  .contact-title {
    font-family: "Poppins", sans-serif;
    font-size: 14px;
    color: var(--warm-grey);
    margin-bottom: 8px;
  }
  .contact-line { font-size: 13px; line-height: 1.4; }
  .contact-links {
    display: flex;
    gap: 16px;
    margin-top: 8px;
    font-size: 13px;
  }
  .contact-links span { display: flex; align-items: center; gap: 5px; }
  .contact-links svg { width: 11px; height: 11px; fill: var(--brand-green); }
</style>
</head>
<body>
  <section class="card card-front">
    <div class="wordmark"><span class="wordmark-dot"></span><span>Bluestone<br>Advisory Management</span></div>
    <div class="contact">
      <p class="contact-name">Dorian Pelkey</p>
      <p class="contact-title">Principle</p>
      <p class="contact-line">Bluestone Advisory &amp; Mgmt, LLC</p>
      <p class="contact-line">348 West 71st Street, 9th FL</p>
      <p class="contact-line">New York, NY 10010</p>
      <div class="contact-links">
        <span><svg viewBox="0 0 24 24" aria-hidden="true"><path d="M6.6 10.8a15 15 0 0 0 6.6 6.6l2.2-2.2c.3-.3.7-.4 1-.2 1.1.4 2.3.6 3.6.6.6 0 1 .4 1 1V20c0 .6-.4 1-1 1A17 17 0 0 1 3 4c0-.6.4-1 1-1h3.5c.6 0 1 .4 1 1 0 1.3.2 2.5.6 3.6.1.3 0 .7-.2 1z"/></svg>917.806.3971</span>
        <span><svg viewBox="0 0 24 24" aria-hidden="true"><circle cx="12" cy="12" r="10"/></svg>bam-hvx.example</span>
      </div>
    </div>
  </section>
  <section class="card card-back">
    <div class="wordmark"><span class="wordmark-dot"></span><span>Bluestone<br>Advisory Management</span></div>
  </section>
</body>
</html>
```